Northcliff Thermal Services Ltd Needs a 2 sided A5 Flyer Design

We need a flyer design for our company to promote Air and ground Source Heat Pumps in the Devon and Cornwall region of the UK.

Our Government has launched the DWB (domestic warmth bonus) a 7 year quarterly payment to offset the cost of installation..
Homeowners currently using OIL or LPG gas for there heating and hot water will save up to 50% on there energy bill by swapping to a heat pump,
Currently education is needed to the potential end user on the benefits of heat pumps,
This flyer will be part of an initial start point to get the homeowner to book a free survey to discuss there options, We are a renewable energy company with great local knowledge, and a wealth of experience ......

KEY points SAVINGS OF UP TO 50% on OIL or LPG heating and hot water systems

DWB PAYMENTS FROM GOVERNMENT FOR 7 years

HONEST IMPARTIAL ADVICE ON SOLUTIONS

FREE SURVEYS ON ALL RENEWABLE SOLUTIONS AND COSTINGS. website www.ncthermal.co.uk have included some potential wording

LOGOS FROM SUPPLIERS

We think side one should be high impact on high oil and LPG gas costs, harm to environment and potential 50% savings with a heat pump. Side 2 to be DWB 7 year quarterly payment and a little about our company offering expertise and free impartial advice and survey

general theme a "striking call to action"

Target Market(s)

Target market is 40 to 60 year old home owners that are off gas grid and use oil or LPG for heating and hot water

Industry/Entity Type

Environment

Font styles to use
Serif
Sans Serif

Colors
33a6d7
f04a50
00a88f
fbed22

Requirements
Must have
• savings 50% on oil or LPG energy costs for heating and hot water

DWB (domestic warmth bonus) government backed payments to offset cost of instalation

7 year payments averaging £1000 a year

FREE impartial advice and surveys

```html
<!DOCTYPE html>
<html lang="en">
<head>
<meta charset="utf-8">
<title>Northcliff Thermal Services Ltd – Heat Pump Flyer</title>
<link rel="stylesheet" href="https://fonts.googleapis.com/css2?family=Noto+Serif:wght@400;700&family=Open+Sans:wght@400;600;700&display=swap">
<style>
  :root {
    --green: #66933a;
    --green-dark: #4f7a2a;
    --black: #000000;
    --white: #ffffff;
    --ink: #1f1f1f;
    --page-bg: #e6e6e4;
    --brand-red: #d8232a;
    --brand-navy: #1d2f5c;
    --brand-blue: #1f7fc4;
    --badge-grey: #9aa4ad;
  }
  * { margin: 0; padding: 0; box-sizing: border-box; }
  html, body {
    width: 988px; height: 1200px; overflow: hidden;
    background: var(--page-bg);
  }
  .flyer {
    position: absolute; left: 56px; top: 20px;
    width: 711px; height: 943px;
    background: var(--white);
    transform: scale(1.2302); transform-origin: 0 0;
    overflow: hidden;
    font-family: "Open Sans", Arial, sans-serif;
  }
  .flyer-shapes { position: absolute; inset: 0; }
  .brand {
    position: absolute; left: 398px; top: 78px; width: 283px;
    text-align: center; color: var(--ink);
    font-family: "Open Sans", Arial, sans-serif; font-weight: 400;
  }
  .brand-name { font-size: 27px; line-height: 1.05; }
  .brand-sub { font-size: 17px; line-height: 1.4; }
  .key-points {
    position: absolute; left: 340px; top: 203px; width: 344px;
    text-align: right; color: var(--white);
    font-family: "Noto Serif", Georgia, serif; font-weight: 700;
    font-size: 16.6px; line-height: 26px;
  }
  .promo-title {
    position: absolute; left: 88px; top: 658px; width: 537px;
    text-align: center; color: var(--green);
    font-family: "Noto Serif", Georgia, serif; font-weight: 700;
    font-size: 15.6px; line-height: 21px;
  }
  .promo-body {
    position: absolute; left: 40px; top: 720px; width: 632px;
    text-align: center; color: var(--white);
    font-weight: 600; font-size: 12.4px; line-height: 20px;
  }
  .contact {
    position: absolute; left: 156px; top: 797px; width: 422px; height: 40px;
    display: flex; align-items: center; justify-content: center; gap: 8px;
    color: var(--white); font-weight: 700; font-size: 17px;
  }
  .contact svg { flex: none; }
  .contact-gap { width: 6px; }
  .supplier {
    position: absolute; top: 860px; height: 83px;
    display: flex; align-items: center; justify-content: center;
    font-family: "Open Sans", Arial, sans-serif; font-weight: 700; font-size: 22px;
  }
  .supplier-harbrook { left: 28px; width: 163px; color: var(--brand-red); }
  .supplier-velmari { left: 201px; width: 143px; color: var(--brand-navy); }
  .supplier-thermaris { left: 352px; width: 174px; color: var(--brand-blue); }
  .approval-label {
    position: absolute; left: 553px; top: 868px;
    font-size: 9px; color: #6b6b6b; letter-spacing: 0.2px;
  }
</style>
</head>
<body>
<div class="flyer">
  <svg class="flyer-shapes" width="711" height="943" viewBox="0 0 711 943">
    <defs>
      <linearGradient id="plantRoomTones" x1="0" y1="0" x2="1" y2="1">
        <stop offset="0" stop-color="#c48a5f"/>
        <stop offset="0.5" stop-color="#a39a8e"/>
        <stop offset="1" stop-color="#6f6a62"/>
      </linearGradient>
      <linearGradient id="houseTones" x1="0" y1="0" x2="0" y2="1">
        <stop offset="0" stop-color="#8fb6e6"/>
        <stop offset="1" stop-color="#9b5a43"/>
      </linearGradient>
      <linearGradient id="conservatoryTones" x1="0" y1="0" x2="0" y2="1">
        <stop offset="0" stop-color="#d7d7d2"/>
        <stop offset="1" stop-color="#6f6248"/>
      </linearGradient>
      <linearGradient id="cylinderTones" x1="0" y1="0" x2="1" y2="0">
        <stop offset="0" stop-color="#9da4a8"/>
        <stop offset="1" stop-color="#d9dcdc"/>
      </linearGradient>
    </defs>

    <rect x="0" y="125" width="711" height="415" fill="var(--green)"/>

    <path d="M398 0 H681 V150 a18 18 0 0 1 -18 18 H416 a18 18 0 0 1 -18 -18 Z" fill="var(--white)"/>

    <polygon points="0,0 193,0 365,190 88,470 0,385" fill="none" stroke="var(--white)" stroke-width="30" stroke-linejoin="round"/>
    <polygon points="0,0 193,0 365,190 88,470 0,385" fill="url(#plantRoomTones)" stroke="var(--black)" stroke-width="9" stroke-linejoin="round"
      role="img" aria-label="Photo of a plant room with copper pipework and pressure gauges"/>

    <rect x="28" y="513" width="200" height="128" rx="16" fill="var(--white)"/>
    <rect x="257" y="513" width="200" height="128" rx="16" fill="var(--white)"/>
    <rect x="484" y="513" width="200" height="128" rx="16" fill="var(--white)"/>

    <rect x="40" y="523" width="176" height="108" rx="14" fill="var(--black)"/>
    <rect x="47" y="530" width="162" height="94" rx="9" fill="url(#houseTones)" role="img" aria-label="Photo of a row of brick houses"/>
    <rect x="269" y="523" width="176" height="108" rx="14" fill="var(--black)"/>
    <rect x="276" y="530" width="162" height="94" rx="9" fill="url(#conservatoryTones)" role="img" aria-label="Photo of a stone house with a glass orangery"/>
    <rect x="496" y="523" width="176" height="108" rx="14" fill="var(--black)"/>
    <rect x="503" y="530" width="162" height="94" rx="9" fill="url(#cylinderTones)" role="img" aria-label="Photo of an insulated hot water cylinder installation"/>

    <rect x="29" y="667" width="654" height="130" rx="16" fill="var(--black)"/>
    <rect x="88" y="655" width="537" height="52" rx="12" fill="var(--white)"/>

    <path d="M156 797 H578 V823 a14 14 0 0 1 -14 14 H170 a14 14 0 0 1 -14 -14 Z" fill="var(--green)"/>

    <rect x="0" y="883" width="711" height="60" fill="var(--black)"/>
    <rect x="191" y="860" width="10" height="23" fill="var(--black)"/>
    <rect x="344" y="860" width="8" height="23" fill="var(--black)"/>
    <rect x="526" y="860" width="8" height="23" fill="var(--black)"/>
    <rect x="28" y="860" width="163" height="83" fill="var(--white)"/>
    <rect x="201" y="860" width="143" height="83" fill="var(--white)"/>
    <rect x="352" y="860" width="174" height="83" fill="var(--white)"/>
    <rect x="534" y="860" width="149" height="83" fill="var(--white)"/>
    <line x1="545" y1="866" x2="545" y2="925" stroke="#9a9a9a" stroke-width="1"/>
    <circle cx="575" cy="905" r="18" fill="var(--badge-grey)"/>
    <rect x="625" y="888" width="34" height="34" fill="var(--badge-grey)"/>
  </svg>

  <div class="brand">
    <div class="brand-name">Northcliff Thermal</div>
    <div class="brand-sub">Services Ltd</div>
  </div>

  <p class="key-points">
    SAVINGS OF UP TO 50% on<br>
    OIL or LPG heating and hot<br>
    water systems<br>
    DWB PAYMENTS FROM<br>
    GOVERNMENT FOR 7 years<br>
    HONEST IMPARTIAL ADVICE<br>
    ON SOLUTIONS FREE<br>
    SURVEYS ON ALL<br>
    RENEWABLE<br>
    SOLUTIONS AND COSTINGS.
  </p>

  <h2 class="promo-title">Our company to promote Air and ground Source Heat<br>Pumps in the Devon and Cornwall region of the UK.</h2>

  <p class="promo-body">
    Homeowners currently using OIL or LPG gas for there heating and hot water will save up to<br>
    50% on there energy bill by swapping to a heat pump,Currently education is needed to the<br>
    potential end user on the benefits of heat pumps
  </p>

  <div class="contact">
    <svg width="17" height="17" viewBox="0 0 20 20" aria-hidden="true">
      <circle cx="10" cy="10" r="8.5" fill="none" stroke="#fff" stroke-width="1.6"/>
      <ellipse cx="10" cy="10" rx="3.8" ry="8.5" fill="none" stroke="#fff" stroke-width="1.4"/>
      <line x1="1.5" y1="10" x2="18.5" y2="10" stroke="#fff" stroke-width="1.4"/>
      <line x1="3" y1="5.5" x2="17" y2="5.5" stroke="#fff" stroke-width="1.2"/>
      <line x1="3" y1="14.5" x2="17" y2="14.5" stroke="#fff" stroke-width="1.2"/>
    </svg>
    <span>www.ncthermal.co.uk</span>
    <span class="contact-gap"></span>
    <svg width="18" height="18" viewBox="0 0 20 20" aria-hidden="true">
      <rect x="0" y="0" width="20" height="20" rx="4" fill="#fff"/>
      <path d="M6.5 4.5 l2 3 -1.3 1.3 c0.8 1.6 1.9 2.7 3.5 3.5 l1.3 -1.3 3 2 -1.2 2.2 c-4.5 0 -8.8 -4.3 -8.8 -8.8 Z" fill="var(--green)"/>
    </svg>
    <span>01752 480913</span>
  </div>

  <div class="supplier supplier-harbrook">Harbrook</div>
  <div class="supplier supplier-velmari">Velmari</div>
  <div class="supplier supplier-thermaris">Thermaris</div>
  <div class="approval-label">APPROVED INSTALLER</div>
</div>
</body>
</html>
```